Boutique personal training and fitness studio - banner ad design

We need a 'revolving' banner ad designed for our personal training and fitness studio. There are three separate offers (i.e. 3 pages to the advertisements)
Offer 1
PT Starter Pack
3 personal training sessions
$119
New clients only
Offer 2
Group fitness
2 weeks unlimited group fitness classes
$29
New clients only
Offer 3
Strength starter pack
2 weeks unlimited group fitness classes and 2 PT sessions
$89
New clients only
Please do not put the words "Offer 1, 2 or 3" in the ads - just the text following each offer.
Each advertisement should be sized to fit across around half of the webpage and be in landscape format.
Each advertisement should have a suitable picture (no cartoons) and should be complimentary to the existing website.
Each advertisement should also include the logo (attached)
www.harrowdaleliftroom.com.au
Training

```html
<!DOCTYPE html>
<html lang="en">
<head>
<meta charset="utf-8">
<title>Harrowdale Lift Room – Offer Banners</title>
<link href="https://fonts.googleapis.com/css2?family=Open+Sans:wght@400;600;700&family=Oswald:wght@500&display=swap" rel="stylesheet">
<style>
  :root{
    --page:#ffffff;
    --panel:#e9e8ec;
    --band:#0d0d0d;
    --red:#b5191f;
    --red-dark:#7e0c10;
    --red-light:#c9262b;
    --ink:#1a1a1a;
    --logo:#c8c8c8;
    --white:#ffffff;
  }
  html,body{margin:0;padding:0;}
  body{
    width:733px;height:1200px;overflow:hidden;
    background:var(--page);
    position:relative;
    font-family:"Open Sans",Arial,sans-serif;
  }
  .banner{
    position:absolute;left:11px;width:710px;height:355px;
    background:var(--panel);overflow:hidden;
  }
  .banner--pt{top:19px;}
  .banner--group{top:419px;}
  .banner--strength{top:819px;}
  .banner__art{position:absolute;inset:0;width:710px;height:355px;}
  .brand{
    position:absolute;left:20px;top:44px;
    font-weight:700;font-size:13px;letter-spacing:.5px;color:var(--logo);
    display:flex;align-items:center;gap:6px;
  }
  .brand__dot{width:9px;height:9px;border-radius:50%;background:var(--logo);}
  .offer-title,.offer-line,.offer-count{
    position:absolute;margin:0;color:var(--red);line-height:1;
    font-family:"Open Sans",Arial,sans-serif;white-space:nowrap;
  }
  .offer-title{font-size:30px;font-weight:600;left:32px;}
  .offer-title--compact{font-size:28px;}
  .offer-count{font-size:56px;font-weight:700;left:30px;}
  .offer-count--large{font-size:72px;}
  .offer-line{font-size:27px;font-weight:600;}
  .offer-line--small{font-size:19px;font-weight:600;}
  .new-clients{
    position:absolute;left:275px;top:273px;margin:0;
    font-size:16px;color:var(--ink);line-height:1;
  }
  .cta{
    position:absolute;left:231px;top:291px;height:56px;display:flex;
    box-shadow:0 1px 2px rgba(0,0,0,.35);
  }
  .cta__price,.cta__book{
    display:flex;align-items:center;justify-content:center;color:var(--white);
    background:linear-gradient(180deg,var(--red-light),var(--red-dark));
  }
  .cta__price{width:101px;font-size:37px;font-weight:400;letter-spacing:-1px;}
  .cta__book{
    width:132px;margin-left:3px;
    font-family:"Oswald","Arial Narrow",sans-serif;font-weight:500;font-size:28px;
  }
</style>
</head>
<body>

<section class="banner banner--pt">
  <svg class="banner__art" viewBox="0 0 710 355">
    <defs>
      <linearGradient id="photo-pt" x1="0" y1="0" x2="1" y2="1">
        <stop offset="0" stop-color="#3d63b8"/><stop offset=".45" stop-color="#2a2f3a"/><stop offset=".7" stop-color="#c9a08a"/><stop offset="1" stop-color="#4c6bc0"/>
      </linearGradient>
      <radialGradient id="glow-pt" cx=".55" cy=".3" r=".5">
        <stop offset="0" stop-color="#d8dbe8" stop-opacity=".45"/><stop offset="1" stop-color="#d8dbe8" stop-opacity="0"/>
      </radialGradient>
    </defs>
    <g role="img" aria-label="Photo: trainer coaching a woman through a sit-up on a blue gym mat">
      <path d="M135 0H710V338Q430 150 135 0Z" fill="url(#photo-pt)"/>
      <path d="M135 0H710V338Q430 150 135 0Z" fill="url(#glow-pt)"/>
    </g>
    <path d="M0 0H135Q430 150 710 338V352Q330 150 0 100Z" fill="var(--band)"/>
    <path d="M135 0Q430 150 710 338" fill="none" stroke="var(--red)" stroke-width="2"/>
    <path d="M0 100Q330 150 710 352" fill="none" stroke="var(--red)" stroke-width="2"/>
  </svg>
  <div class="brand"><span class="brand__dot"></span>HARROWDALE LIFT ROOM</div>
  <h2 class="offer-title" style="top:174px">PT Starter Pack</h2>
  <p class="offer-count" style="top:218px">3</p>
  <p class="offer-line" style="left:65px;top:237px">Personal Training</p>
  <p class="offer-line" style="left:72px;top:270px">Sessions</p>
  <p class="new-clients">New Clients Only</p>
  <div class="cta"><span class="cta__price">$119</span><span class="cta__book">BOOK NOW</span></div>
</section>

<section class="banner banner--group">
  <svg class="banner__art" viewBox="0 0 710 355">
    <defs>
      <linearGradient id="photo-group" x1="0" y1="0" x2="1" y2="1">
        <stop offset="0" stop-color="#d9c7ab"/><stop offset=".4" stop-color="#8f8a95"/><stop offset=".65" stop-color="#3a3a44"/><stop offset="1" stop-color="#e6e6ea"/>
      </linearGradient>
      <radialGradient id="glow-group" cx=".7" cy=".75" r=".35">
        <stop offset="0" stop-color="#7b5fb0" stop-opacity=".5"/><stop offset="1" stop-color="#7b5fb0" stop-opacity="0"/>
      </radialGradient>
    </defs>
    <g role="img" aria-label="Photo: group fitness class lifting dumbbells on exercise balls">
      <path d="M135 0H710V338Q430 150 135 0Z" fill="url(#photo-group)"/>
      <path d="M135 0H710V338Q430 150 135 0Z" fill="url(#glow-group)"/>
    </g>
    <path d="M0 0H135Q430 150 710 338V352Q330 150 0 100Z" fill="var(--band)"/>
    <path d="M135 0Q430 150 710 338" fill="none" stroke="var(--red)" stroke-width="2"/>
    <path d="M0 100Q330 150 710 352" fill="none" stroke="var(--red)" stroke-width="2"/>
  </svg>
  <div class="brand"><span class="brand__dot"></span>HARROWDALE LIFT ROOM</div>
  <h2 class="offer-title" style="top:162px">Group Fitness</h2>
  <p class="offer-count" style="top:198px">2</p>
  <p class="offer-line" style="left:62px;top:218px">weeks Unlimited</p>
  <p class="offer-line" style="left:64px;top:247px">Group Fitness</p>
  <p class="offer-line" style="left:64px;top:276px">Classes</p>
  <p class="new-clients">New Clients Only</p>
  <div class="cta"><span class="cta__price">$29</span><span class="cta__book">BOOK NOW</span></div>
</section>

<section class="banner banner--strength">
  <svg class="banner__art" viewBox="0 0 710 355">
    <defs>
      <linearGradient id="photo-strength" x1="0" y1="0" x2="1" y2="1">
        <stop offset="0" stop-color="#c9a27a"/><stop offset=".45" stop-color="#2f63b5"/><stop offset=".7" stop-color="#1e2a4a"/><stop offset="1" stop-color="#b98a5c"/>
      </linearGradient>
      <radialGradient id="glow-strength" cx=".3" cy=".2" r=".4">
        <stop offset="0" stop-color="#d23a2e" stop-opacity=".4"/><stop offset="1" stop-color="#d23a2e" stop-opacity="0"/>
      </radialGradient>
    </defs>
    <g role="img" aria-label="Photo: kickboxing class with punching bags in a timber-floored studio">
      <path d="M135 0H710V338Q430 150 135 0Z" fill="url(#photo-strength)"/>
      <path d="M135 0H710V338Q430 150 135 0Z" fill="url(#glow-strength)"/>
    </g>
    <path d="M0 0H135Q430 150 710 338V352Q330 150 0 100Z" fill="var(--band)"/>
    <path d="M135 0Q430 150 710 338" fill="none" stroke="var(--red)" stroke-width="2"/>
    <path d="M0 100Q330 150 710 352" fill="none" stroke="var(--red)" stroke-width="2"/>
  </svg>
  <div class="brand"><span class="brand__dot"></span>HARROWDALE LIFT ROOM</div>
  <h2 class="offer-title offer-title--compact" style="top:188px">Strength Starter Pack</h2>
  <p class="offer-count offer-count--large" style="top:222px">2</p>
  <p class="offer-line offer-line--small" style="left:78px;top:231px">weeks Unlimited Group</p>
  <p class="offer-line offer-line--small" style="left:78px;top:255px">Fitness Classes&nbsp; and</p>
  <p class="offer-line offer-line--small" style="left:78px;top:285px">PT sessions</p>
  <p class="new-clients">New Clients Only</p>
  <div class="cta"><span class="cta__price">$89</span><span class="cta__book">BOOK NOW</span></div>
</section>

</body>
</html>
```